COMMERCIAL DOOR REPAIR
BUSINESS CARDS, LETTERHEAD, ENVELOPES, FAX COVER, EMAIL SIGNATURE
Rob Whitfield
NFPEI Certified Door Inspector
1752 E Pinnell Ln Glendale, AZ 85317
service@robsgatefix.com
www.robsgatefix.com
ROC# 514037
Not sure if font in logo can be used - open to other fonts as well. just no script or femine fonts. Not sure if all items on back will fit - open to re-wording, suggestions, etc.
24 Hour Emergency Services Available Specializing in: Automatic Doors Manual Doors Vitrelon Glass Doors Hollow Metal Doors Revolving Doors Also specializing in: Glass Mirrors Locksmithing Shower Doors Roof Hatches Re-seals Board-Ups

```html
<!DOCTYPE html>
<html lang="en">
<head>
<meta charset="utf-8">
<title>Gatefix Services – Stationery Set</title>
<link rel="stylesheet" href="https://fonts.googleapis.com/css2?family=Open+Sans:wght@400;600;700&display=swap">
<style>
:root{
  --blue:#1d6bbf;
  --blue-dark:#0f4f96;
  --blue-light:#4a95e0;
  --red:#c81f2e;
  --ink:#3a3f47;
  --muted:#8a9099;
  --line:#d5d9df;
  --paper:#ffffff;
  --stage:#e9ebee;
}
*{box-sizing:border-box;margin:0;padding:0}
html,body{width:1200px;height:1070px;overflow:hidden}
body{background:var(--stage);font-family:"Open Sans",Arial,sans-serif;color:var(--ink);position:relative}
.piece{position:absolute;background:var(--paper);box-shadow:0 2px 6px rgba(0,0,0,.18);overflow:hidden}
.band{position:absolute;left:0;bottom:0;width:100%;background:var(--blue);border-top:4px solid var(--red)}
.brand{display:flex;align-items:center;gap:5px}
.brand-mark{width:10px;height:10px;border-radius:50%;background:var(--blue);flex:none}
.brand-name{font-family:"Open Sans",Arial,sans-serif;font-weight:700;color:var(--blue);font-size:12px;white-space:nowrap}
.tiny{font-size:5.5px;line-height:1.5;color:var(--ink)}
.on-blue .brand-mark{background:#fff}
.on-blue .brand-name{color:#fff}

/* envelopes */
.envelope-front{left:35px;top:30px;width:260px;height:125px}
.envelope-front .brand{position:absolute;left:12px;top:12px}
.envelope-front .tiny{position:absolute;left:27px;top:30px}
.envelope-back{left:322px;top:30px;width:262px;height:125px;background:linear-gradient(180deg,var(--blue-light),var(--blue-dark))}
.envelope-back .flap{position:absolute;left:0;top:0;width:100%;height:60px}
.envelope-back .brand{position:absolute;left:50%;top:12px;transform:translateX(-50%)}

/* business cards */
.card{width:155px;height:88px;top:30px}
.card-front{left:612px}
.card-front .brand{position:absolute;left:10px;top:10px}
.card-front .brand-name{font-size:10px}
.card-front .card-name{position:absolute;left:10px;top:30px;font-size:8px;font-weight:700;color:var(--blue)}
.card-front .tiny{position:absolute;left:10px;top:42px;font-size:5px}
.card-back{left:780px;background:linear-gradient(180deg,var(--blue-light),var(--blue-dark));color:#fff;padding:9px 10px}
.card-back h3{font-size:6.5px;font-weight:700;margin-bottom:3px}
.card-back .cols{display:flex;gap:10px;font-size:5px;line-height:1.45}

/* letter-size sheets */
.sheet{width:262px;height:325px;top:170px}
.letterhead{left:35px}
.fax{left:322px}
.sheet .brand{position:absolute;left:14px;top:14px}
.sheet .head-info{position:absolute;left:29px;top:31px}
.fax h2{position:absolute;right:14px;top:12px;font-weight:700;font-size:13px;color:var(--blue)}
.fax .fields{position:absolute;left:14px;top:66px;width:234px}
.fax .field{display:flex;gap:4px;font-size:6px;border-bottom:1px solid var(--line);padding:4px 0}
.fax .field b{width:30px;color:var(--blue)}
.fax .checks{display:flex;gap:10px;font-size:5.5px;margin-top:8px}
.fax .checks span::before{content:"";display:inline-block;width:5px;height:5px;border:1px solid var(--muted);margin-right:3px;vertical-align:-1px}

/* invoice & quote */
.bill{width:265px;height:440px;top:160px}
.invoice{left:612px}
.quote{left:895px}
.bill .brand{position:absolute;left:14px;top:14px}
.bill .head-info{position:absolute;left:29px;top:31px}
.bill h2{position:absolute;right:14px;top:12px;font-weight:700;font-size:12px;color:var(--blue)}
.bill .meta{position:absolute;right:14px;top:34px;font-size:5.5px;text-align:right;line-height:1.6}
.bill .bill-to{position:absolute;left:14px;top:66px;width:110px;border:1px solid var(--line);height:42px;font-size:5.5px;padding:3px}
.bill .bill-to b{color:var(--blue)}
.bill table{position:absolute;left:14px;top:118px;width:237px;border-collapse:collapse;font-size:5.5px}
.bill th{background:var(--blue);color:#fff;font-weight:600;padding:3px;text-align:left}
.bill td{border:1px solid var(--line);height:13px;padding:0 3px}
.bill .totals{position:absolute;right:14px;top:352px;font-size:5.5px;width:90px}
.bill .totals div{display:flex;justify-content:space-between;border-bottom:1px solid var(--line);padding:2px 0}
.bill .totals .grand{color:var(--blue);font-weight:700}
.bill .thanks{position:absolute;left:14px;top:362px;font-size:6px;color:var(--blue);font-weight:600}

/* email signatures */
.signature{top:615px;height:115px;display:flex;align-items:center;gap:12px;padding:0 14px}
.sig-left{left:75px;width:510px}
.sig-right{left:612px;width:548px}
.sig-logo{width:170px;height:70px;background:linear-gradient(180deg,var(--blue-light),var(--blue-dark));display:flex;align-items:center;justify-content:center;flex:none}
.sig-logo .brand-name{font-size:14px}
.sig-name{font-size:13px;font-weight:700;color:var(--blue)}
.sig-title{font-size:8px;color:var(--ink);margin-bottom:5px}
.sig-contact{font-size:7px;line-height:1.55;display:grid;grid-template-columns:auto auto;gap:0 14px}
.sig-contact .ic{color:var(--red);font-weight:700;margin-right:3px}
.signature .edge{position:absolute;left:0;bottom:0;width:100%;height:5px;background:linear-gradient(90deg,var(--blue) 70%,var(--red) 70%)}

/* folder */
.folder-front{left:75px;top:750px;width:510px;height:305px}
.folder-front .band{height:150px;border-top-width:10px;background:linear-gradient(180deg,var(--blue-light),var(--blue-dark))}
.folder-front .brand{position:absolute;left:50%;top:72px;transform:translateX(-50%)}
.folder-front .brand-mark{width:20px;height:20px}
.folder-front .brand-name{font-size:24px}
.folder-front .folder-tag{position:absolute;left:0;width:100%;text-align:center;top:106px;font-size:7px;letter-spacing:2px;color:var(--muted)}
.folder-front .foot{position:absolute;left:14px;bottom:10px;font-size:6px;color:#fff}
.folder-inside{left:612px;top:750px;width:548px;height:305px;background:#f4f6f9}
.folder-inside .spine{position:absolute;left:50%;top:0;width:1px;height:100%;background:var(--line)}
.pocket{position:absolute;bottom:0;width:274px;height:130px;background:#eaeef3;border-top:1px solid var(--line)}
.pocket-left{left:0;clip-path:polygon(0 12%,100% 0,100% 100%,0 100%)}
.pocket-right{right:0;clip-path:polygon(0 0,100% 12%,100% 100%,0 100%)}
.slot-card{position:absolute;left:380px;top:205px;width:90px;height:52px;background:#fff;box-shadow:0 1px 3px rgba(0,0,0,.2)}
.slot-card .brand{position:absolute;left:5px;top:6px;gap:3px}
.slot-card .brand-mark{width:6px;height:6px}
.slot-card .brand-name{font-size:7px}
.slot-card .edge{position:absolute;left:0;bottom:0;width:100%;height:8px;background:var(--blue)}
</style>
</head>
<body>

<!-- envelopes -->
<section class="piece envelope-front">
  <div class="brand"><span class="brand-mark"></span><span class="brand-name">Gatefix Services</span></div>
  <p class="tiny">1752 E Pinnell Ln<br>Glendale, AZ 85317</p>
  <div class="band" style="height:26px"></div>
</section>

<section class="piece envelope-back on-blue">
  <svg class="flap" viewBox="0 0 300 70" preserveAspectRatio="none" aria-hidden="true"><path d="M0 0 L300 0 L150 60Z" fill="rgba(255,255,255,.12)"/></svg>
  <div class="brand"><span class="brand-mark"></span><span class="brand-name">Gatefix Services</span></div>
</section>

<!-- business cards -->
<section class="piece card card-front">
  <div class="brand"><span class="brand-mark"></span><span class="brand-name">Gatefix Services</span></div>
  <p class="card-name">Rob Whitfield</p>
  <p class="tiny">NFPEI Certified Door Inspector<br>(623) 555-0148 · service@robsgatefix.com</p>
  <div class="band" style="height:14px;border-top-width:3px"></div>
</section>

<section class="piece card card-back">
  <h3>24 Hour Emergency Services Available</h3>
  <div class="cols">
    <p>Automatic Doors<br>Manual Doors<br>Vitrelon Glass Doors<br>Hollow Metal Doors<br>Revolving Doors</p>
    <p>Glass Mirrors<br>Locksmithing<br>Shower Doors<br>Roof Hatches<br>Re-seals · Board-Ups</p>
  </div>
</section>

<!-- letterhead -->
<section class="piece sheet letterhead">
  <div class="brand"><span class="brand-mark"></span><span class="brand-name">Gatefix Services</span></div>
  <p class="tiny head-info">1752 E Pinnell Ln, Glendale, AZ 85317<br>(623) 555-0148 · www.robsgatefix.com</p>
  <div class="band" style="height:30px"></div>
</section>

<!-- fax cover -->
<section class="piece sheet fax">
  <div class="brand"><span class="brand-mark"></span><span class="brand-name">Gatefix Services</span></div>
  <p class="tiny head-info">1752 E Pinnell Ln, Glendale, AZ 85317<br>Fax (623) 555-0149</p>
  <h2>FAX</h2>
  <div class="fields">
    <div class="field"><b>To:</b></div>
    <div class="field"><b>From:</b></div>
    <div class="field"><b>Fax:</b></div>
    <div class="field"><b>Date:</b></div>
    <div class="field"><b>Re:</b></div>
    <div class="checks"><span>Urgent</span><span>For Review</span><span>Please Reply</span></div>
  </div>
  <div class="band" style="height:30px"></div>
</section>

<!-- invoice -->
<section class="piece bill invoice">
  <div class="brand"><span class="brand-mark"></span><span class="brand-name">Gatefix Services</span></div>
  <p class="tiny head-info">1752 E Pinnell Ln<br>Glendale, AZ 85317</p>
  <h2>INVOICE</h2>
  <p class="meta">Invoice No.<br>Date<br>Due Date</p>
  <div class="bill-to"><b>Bill To</b></div>
  <table>
    <thead><tr><th>Description</th><th>Qty</th><th>Rate</th><th>Amount</th></tr></thead>
    <tbody>
      <tr><td></td><td></td><td></td><td></td></tr><tr><td></td><td></td><td></td><td></td></tr>
      <tr><td></td><td></td><td></td><td></td></tr><tr><td></td><td></td><td></td><td></td></tr>
      <tr><td></td><td></td><td></td><td></td></tr><tr><td></td><td></td><td></td><td></td></tr>
      <tr><td></td><td></td><td></td><td></td></tr><tr><td></td><td></td><td></td><td></td></tr>
      <tr><td></td><td></td><td></td><td></td></tr><tr><td></td><td></td><td></td><td></td></tr>
      <tr><td></td><td></td><td></td><td></td></tr><tr><td></td><td></td><td></td><td></td></tr>
      <tr><td></td><td></td><td></td><td></td></tr><tr><td></td><td></td><td></td><td></td></tr>
    </tbody>
  </table>
  <p class="thanks">Thank you for your business</p>
  <div class="totals"><div><span>Subtotal</span></div><div><span>Tax</span></div><div class="grand"><span>Total</span></div></div>
  <div class="band" style="height:28px"></div>
</section>

<!-- quote -->
<section class="piece bill quote">
  <div class="brand"><span class="brand-mark"></span><span class="brand-name">Gatefix Services</span></div>
  <p class="tiny head-info">1752 E Pinnell Ln<br>Glendale, AZ 85317</p>
  <h2>QUOTE</h2>
  <p class="meta">Quote No.<br>Date<br>Valid Until</p>
  <div class="bill-to"><b>Prepared For</b></div>
  <table>
    <thead><tr><th>Description</th><th>Qty</th><th>Rate</th><th>Amount</th></tr></thead>
    <tbody>
      <tr><td></td><td></td><td></td><td></td></tr><tr><td></td><td></td><td></td><td></td></tr>
      <tr><td></td><td></td><td></td><td></td></tr><tr><td></td><td></td><td></td><td></td></tr>
      <tr><td></td><td></td><td></td><td></td></tr><tr><td></td><td></td><td></td><td></td></tr>
      <tr><td></td><td></td><td></td><td></td></tr><tr><td></td><td></td><td></td><td></td></tr>
      <tr><td></td><td></td><td></td><td></td></tr><tr><td></td><td></td><td></td><td></td></tr>
      <tr><td></td><td></td><td></td><td></td></tr><tr><td></td><td></td><td></td><td></td></tr>
      <tr><td></td><td></td><td></td><td></td></tr><tr><td></td><td></td><td></td><td></td></tr>
    </tbody>
  </table>
  <p class="thanks">Quote valid for 30 days</p>
  <div class="totals"><div><span>Subtotal</span></div><div><span>Tax</span></div><div class="grand"><span>Total</span></div></div>
  <div class="band" style="height:28px"></div>
</section>

<!-- email signatures -->
<section class="piece signature sig-left">
  <div class="sig-logo on-blue"><div class="brand"><span class="brand-mark"></span><span class="brand-name">Gatefix Services</span></div></div>
  <div>
    <p class="sig-name">Rob Whitfield</p>
    <p class="sig-title">NFPEI Certified Door Inspector</p>
    <div class="sig-contact">
      <span><span class="ic">☎</span>(623) 555-0148</span><span>1752 E Pinnell Ln</span>
      <span><span class="ic">✉</span>service@robsgatefix.com</span><span>Glendale, AZ 85317</span>
      <span><span class="ic">➜</span>www.robsgatefix.com</span><span>Fax (623) 555-0149</span>
    </div>
  </div>
  <span class="edge"></span>
</section>

<section class="piece signature sig-right">
  <div class="sig-logo on-blue"><div class="brand"><span class="brand-mark"></span><span class="brand-name">Gatefix Services</span></div></div>
  <div>
    <p class="sig-name">Rob Whitfield</p>
    <p class="sig-title">NFPEI Certified Door Inspector</p>
    <div class="sig-contact">
      <span><span class="ic">☎</span>(623) 555-0148</span><span><span class="ic">⌂</span>1752 E Pinnell Ln, Glendale, AZ 85317</span>
      <span><span class="ic">✉</span>service@robsgatefix.com</span><span><span class="ic">➜</span>www.robsgatefix.com</span>
    </div>
  </div>
  <span class="edge"></span>
</section>

<!-- presentation folder -->
<section class="piece folder-front">
  <div class="brand"><span class="brand-mark"></span><span class="brand-name">Gatefix Services</span></div>
  <p class="folder-tag">COMMERCIAL DOOR REPAIR</p>
  <div class="band"></div>
  <p class="foot">1752 E Pinnell Ln, Glendale, AZ 85317 · www.robsgatefix.com</p>
</section>

<section class="piece folder-inside">
  <span class="spine"></span>
  <div class="pocket pocket-left"></div>
  <div class="pocket pocket-right"></div>
  <div class="slot-card">
    <div class="brand"><span class="brand-mark"></span><span class="brand-name">Gatefix Services</span></div>
    <span class="edge"></span>
  </div>
</section>

</body>
</html>
```